Corwick Habitat Web

We just need an update/re-design of our existing web site that would include our new company logo and some new photo's. Our current web site can be viewed at www.corwickhabitat.com.au. We would require something very similar to what we have at the moment in terms of content it should all be the same.
The web site would basically act more as a portfolio than one that would generate more business.
We are after a very modern and simple design and maybe something where we can upload our own project photo's and project descriptions as we complete them.

Industry/Entity Type

It Company

```html
<!DOCTYPE html>
<html lang="en">
<head>
<meta charset="utf-8">
<title>Corwick Habitat</title>
<link href="https://fonts.googleapis.com/css2?family=Lato:wght@300;400;700&family=Open+Sans:wght@400;600&family=Roboto:wght@400&display=swap" rel="stylesheet">
<style>
  :root {
    --ink: #111111;
    --text: #3a3a3a;
    --steel: #4b7796;
    --steel-dark: #3d657f;
    --black: #000000;
    --white: #ffffff;
    --wood-dark: #4a1f12;
    --wood-mid: #7a3a22;
    --wood-light: #9a5233;
    --logo-grey: #6b6b6b;
  }
  * { margin: 0; padding: 0; box-sizing: border-box; }
  html, body { width: 1200px; height: 1070px; overflow: hidden; background: var(--white); }
  body { position: relative; font-family: "Open Sans", sans-serif; color: var(--text); }

  .site-header { position: absolute; left: 0; top: 0; width: 1200px; height: 84px; }
  .brand { position: absolute; left: 121px; top: 18px; font-family: "Lato", sans-serif; font-weight: 300; font-size: 38px; color: var(--logo-grey); letter-spacing: 0.5px; line-height: 1; }

  .main-nav { position: absolute; left: 120px; top: 84px; width: 960px; height: 42px; background: var(--black); }
  .main-nav ul { list-style: none; display: flex; height: 100%; }
  .main-nav li { font-family: "Roboto", sans-serif; font-size: 11px; letter-spacing: 1.2px; color: var(--white); text-transform: uppercase; display: flex; align-items: center; justify-content: center; height: 100%; }
  .nav-home { width: 96px; }
  .nav-projects { width: 145px; background: var(--steel); }
  .nav-services { width: 140px; }
  .nav-contact { width: 120px; border-left: 1px solid #555; height: 24px !important; margin-top: 9px; }
  .search { position: absolute; left: 746px; top: 8px; width: 195px; height: 26px; background: var(--white); border-radius: 4px; border: 1px solid #ccc; }
  .search span { position: absolute; left: 11px; top: 6px; font-family: Georgia, serif; font-style: italic; font-size: 11px; color: #999; }
  .search svg { position: absolute; right: 8px; top: 5px; }

  .hero-band { position: absolute; left: 0; top: 126px; width: 1200px; height: 497px;
    background: linear-gradient(90deg, var(--wood-dark), var(--wood-mid) 4%, var(--wood-light) 6%, var(--wood-mid) 9%, var(--wood-dark) 10%, var(--wood-dark) 90%, var(--wood-mid) 92%, var(--wood-light) 95%, var(--wood-mid) 97%, var(--wood-dark)); }
  .hero-frame { position: absolute; left: 120px; top: 0; width: 960px; height: 497px; background: var(--steel); padding: 6px 7px 6px 7px; }
  .hero-photo { width: 100%; height: 100%; background: linear-gradient(180deg, #2b2f3a 0%, #e6e4df 40%, #c9c2b3 75%, #9d947f 100%); }

  .intro { position: absolute; left: 128px; top: 646px; width: 580px; }
  .intro h1 { font-family: "Lato", sans-serif; font-weight: 700; font-size: 21px; color: var(--ink); margin-bottom: 14px; }
  .intro p, .intro li { font-size: 13.4px; line-height: 20px; padding-left: 3px; }
  .intro ul { list-style: none; padding-left: 24px; }
  .intro li { font-weight: 600; color: var(--ink); }
  .intro li::before { content: ">"; margin-right: 8px; }

  .projects-panel { position: absolute; left: 732px; top: 623px; width: 348px; height: 361px; background: var(--steel); }
  .projects-panel h2 { position: absolute; left: 27px; top: 24px; font-family: "Lato", sans-serif; font-weight: 700; font-size: 21px; color: var(--white); }
  .thumb { position: absolute; left: 29px; width: 280px; height: 72px; border: 2px solid var(--white); }
  .thumb-1 { top: 65px; background: linear-gradient(180deg, #2e2e2e, #9a9891 60%, #5d5b57); }
  .thumb-2 { top: 149px; background: linear-gradient(180deg, #bcd0e0, #4d6f8c 55%, #5a3428 80%, #8a8680); }
  .thumb-3 { top: 233px; background: linear-gradient(180deg, #d9dfe3, #8a7a6a 50%, #3d3d3d 85%, #6c6c6a); }
  .scrollbar { position: absolute; left: 330px; top: 65px; width: 3px; height: 240px; background: var(--white); }
  .scrollbar i { position: absolute; left: 0; top: 70px; width: 3px; height: 40px; background: #1c2b35; }

  .site-footer { position: absolute; left: 0; top: 984px; width: 1200px; height: 86px; background: var(--black); }
  .footer-brand { position: absolute; left: 131px; top: 27px; font-family: "Lato", sans-serif; font-weight: 300; font-size: 20px; color: #9a9a9a; }
  .footer-contact { position: absolute; right: 139px; top: 23px; text-align: right; font-size: 10px; line-height: 15px; color: var(--white); }
</style>
</head>
<body>
  <header class="site-header">
    <div class="brand">corwick habitat</div>
  </header>

  <nav class="main-nav">
    <ul>
      <li class="nav-home">Home</li>
      <li class="nav-projects">Recent Projects</li>
      <li class="nav-services">Our Services</li>
      <li class="nav-contact">Contact Us</li>
    </ul>
    <div class="search">
      <span>Search</span>
      <svg width="14" height="14" viewBox="0 0 14 14"><circle cx="5.5" cy="5.5" r="4" fill="none" stroke="#999" stroke-width="1.6"/><line x1="8.5" y1="8.5" x2="12.5" y2="12.5" stroke="#999" stroke-width="2"/></svg>
    </div>
  </nav>

  <section class="hero-band">
    <div class="hero-frame">
      <div class="hero-photo" role="img" aria-label="Office lobby interior with dark acoustic ceiling baffles, timber battens, glass stair and tiled floor"></div>
    </div>
  </section>

  <main class="intro">
    <h1>Corwick Habitat Pty Limited</h1>
    <p>Corwick Habitat Pty Ltd was established in 2005 and has been operating in the Sydney area, but has completed numerous projects outside of Sydney.<br>We specialise in the internal fit outs to,</p>
    <ul>
      <li>Industrial Offices</li>
      <li>Multi Storey Offices</li>
      <li>Commercial Projects</li>
      <li>Residential Houses</li>
      <li>External Facades</li>
    </ul>
    <p>The key group of our operating staff have all been involved in the construction industry for well over 20 years.&nbsp; Our employees are skilled and trained and have the experience to deliver the best possible product, safely and on time. At Corwick Habitat we pride ourselves on working together with our clients in providing the best possible service on schedule and within budget</p>
  </main>

  <aside class="projects-panel">
    <h2>Recent Projects</h2>
    <div class="thumb thumb-1" role="img" aria-label="Modern building exterior with cantilevered grey facade"></div>
    <div class="thumb thumb-2" role="img" aria-label="Glazed office building facade reflecting sky"></div>
    <div class="thumb thumb-3" role="img" aria-label="Commercial building frontage with timber and glass panels"></div>
    <div class="scrollbar"><i></i></div>
  </aside>

  <footer class="site-footer">
    <div class="footer-brand">corwick habitat</div>
    <div class="footer-contact">
      4120 Harlow Avenue, Westbrook D.C.<br>
      Tel: 0800-417-662, 1800-529-803<br>
      Email: info@corwickhabitat.com
    </div>
  </footer>
</body>
</html>
```